Building company requiring web site design

We need a web design for a new company based in Sydney called Marlow Building Co. We build and renovate new and existing homes for consumers. We would like to see design that use the colours red and grey. The final design should communicate innovative building but with old fashion quality, great customer service and attention to detail. I have already had a logo and stationary design completed and would like to use the these colour schemes
Updates

Target Market(s)

Home owners, investors

Industry/Entity Type

Building

Coding

Coded - Design and coding required

Number of Pages Required

5+ page

Requirements
Must have
• Home page, contact page, about us page, gallery page and testimonial page
Nice to have
• Contact form

```html
<!DOCTYPE html>
<html lang="en">
<head>
<meta charset="utf-8">
<title>Marlow Building Co.</title>
<link rel="stylesheet" href="https://fonts.googleapis.com/css2?family=Oswald:wght@400;500&family=Roboto:ital,wght@0,400;0,500;1,400&display=swap">
<style>
:root{
  --red:#b5443d;
  --red-dark:#9f3a34;
  --ink:#222;
  --text:#555;
  --muted:#888;
  --grey-band:#f0f0f0;
  --footer-bottom:#161616;
  --white:#fff;
}
*{box-sizing:border-box;margin:0;padding:0}
html,body{width:1200px;height:2679px;overflow:hidden;background:var(--white)}
body{position:relative;font-family:'Roboto',sans-serif;color:var(--text)}
.abs{position:absolute}

/* header */
.site-header{position:absolute;left:0;top:0;width:1200px;height:143px;background:var(--white)}
.brand{position:absolute;left:89px;top:48px;display:flex;align-items:center;gap:12px}
.brand-mark{width:26px;height:26px;background:var(--red)}
.brand-name{font-family:'Roboto',sans-serif;font-weight:500;font-size:22px;color:var(--ink)}
.main-nav{position:absolute;left:441px;top:70px;display:flex;gap:31px;font-size:14px;color:#444;letter-spacing:.3px}
.main-nav .active{color:var(--red)}
.search-btn{position:absolute;left:1068px;top:59px;width:43px;height:38px;border:2px solid #888;border-radius:3px}

/* hero */
.hero{position:absolute;left:0;top:143px;width:1200px;height:589px;
  background:linear-gradient(180deg,#3c4048 0%,#2a2d33 45%,#3a3833 100%)}
.hero-title{position:absolute;left:89px;top:255px;font-family:'Oswald',sans-serif;font-weight:500;font-size:60px;line-height:1;color:var(--white);text-transform:uppercase}
.hero-sub{position:absolute;left:89px;top:320px;font-family:'Oswald',sans-serif;font-weight:400;font-size:46px;line-height:1;color:var(--white)}
.hero-dots{position:absolute;left:96px;top:405px;display:flex;gap:7px}
.hero-dots span{width:10px;height:10px;border-radius:50%;background:var(--white)}
.hero-dots span:first-child{background:var(--red)}

.section-title{position:absolute;left:0;width:1200px;text-align:center;font-size:27px;font-weight:500;color:var(--ink);text-transform:uppercase}
.section-title em{font-style:normal;color:var(--red)}

/* services */
.service{position:absolute;top:850px;width:240px;text-align:center}
.service-icon{width:107px;height:107px;margin:0 auto;border-radius:50%;background:var(--red);border:5px solid #e6e6e6;display:flex;align-items:center;justify-content:center}
.service-name{margin-top:20px;font-size:14px;font-weight:500;color:var(--ink);text-transform:uppercase}
.service-text{margin-top:14px;font-size:11px;line-height:20px;color:var(--muted);padding:0 24px}

/* projects */
.projects{position:absolute;left:0;top:1120px;width:1200px;height:430px;background:var(--grey-band)}
.project{position:absolute;top:120px;width:246px;height:242px;background:var(--white);box-shadow:0 1px 3px rgba(0,0,0,.2)}
.project-photo{width:100%;height:194px}
.project-label{position:absolute;left:0;bottom:0;width:100%;height:48px;background:var(--red);color:var(--white);font-size:13px;line-height:48px;padding-left:12px}
.project-label::after{content:"";position:absolute;right:0;top:0;width:86px;height:48px;background:#2c2c2c;clip-path:polygon(30% 0,100% 0,100% 100%,0 100%)}
.project-go{position:absolute;right:24px;top:16px;width:16px;height:16px;border-radius:50%;background:var(--white);z-index:1}
.slider-arrow{position:absolute;top:1350px}

/* testimonial */
.testimonial{position:absolute;left:0;top:1550px;width:1200px;height:311px;background:linear-gradient(180deg,#b5504a,#a8443e)}
.avatar{position:absolute;left:556px;top:45px;width:96px;height:96px;border-radius:50%;background:#c9b9ae;border:4px solid var(--white)}
.quote{position:absolute;left:150px;top:168px;width:900px;text-align:center;font-size:11.5px;line-height:21px;color:#f4e5e3}
.quote-by{position:absolute;left:0;top:244px;width:1200px;text-align:center;font-style:italic;font-size:15px;color:#f6e9e7}

/* blog */
.post{position:absolute;top:1968px;width:318px}
.post-photo{position:relative;height:193px;border:3px solid #eee}
.post-date{position:absolute;left:0;top:48px;width:50px;text-align:center;color:var(--white)}
.post-date .day{display:block;background:var(--red);font-size:20px;font-weight:500;padding-top:6px;height:50px;line-height:22px}
.post-date .day small{display:block;font-size:10px;line-height:14px}
.post-date .year{display:block;background:#2c2c2c;font-size:14px;height:34px;line-height:34px}
.post-title{margin-top:18px;font-size:14.5px;color:#333}
.post-text{margin-top:12px;font-size:11px;line-height:18px;color:var(--muted)}
.post-more{margin-top:14px;font-size:11px;color:var(--red)}

/* footer */
.site-footer{position:absolute;left:0;top:2350px;width:1200px;height:222px;background:var(--red);color:#f5dcd9}
.footer-col{position:absolute;top:42px}
.footer-col h4{font-size:14.5px;font-weight:500;color:var(--white);text-transform:uppercase;margin-bottom:20px}
.footer-links li{list-style:none;font-size:11px;line-height:24.5px}
.footer-links li::before{content:"▸";font-size:9px;margin-right:6px}
.footer-text{font-size:10.5px;line-height:18px;text-align:justify}
.newsletter{display:flex;margin-top:14px}
.newsletter input{width:150px;height:28px;border:0;padding-left:10px;font-size:10px;font-family:'Roboto',sans-serif}
.newsletter button{width:54px;height:28px;border:0;background:#161616;color:var(--white);font-size:11px;font-family:'Roboto',sans-serif}
.social{display:flex;gap:14px;margin-top:14px}
.social span{width:32px;height:32px;border-radius:50%;border:1px solid #f3d0cc}
.footer-bottom{position:absolute;left:0;top:2572px;width:1200px;height:107px;background:var(--footer-bottom);color:var(--white);font-size:12px;text-align:center;line-height:107px}
</style>
</head>
<body>

<header class="site-header">
  <div class="brand"><span class="brand-mark"></span><span class="brand-name">Marlow Building Co.</span></div>
  <nav class="main-nav">
    <span class="active">HOME</span><span>ABOUT</span><span>PROJECTS</span><span>SERVICES</span><span>PARTNERS</span><span>BLOG</span><span>CONTACTS</span>
  </nav>
  <div class="search-btn">
    <svg width="39" height="34" viewBox="0 0 39 34"><circle cx="18" cy="15" r="6" fill="none" stroke="#666" stroke-width="2"/><line x1="22.5" y1="19.5" x2="27" y2="24" stroke="#666" stroke-width="2"/></svg>
  </div>
</header>

<section class="hero" role="img" aria-label="Night aerial view of a city skyline with tall towers">
  <h1 class="hero-title">Marlow Building Co</h1>
  <p class="hero-sub">We build and renovate new</p>
  <div class="hero-dots"><span></span><span></span><span></span><span></span><span></span></div>
</section>

<h2 class="section-title" style="top:782px">Our <em>Services</em></h2>

<div class="service" style="left:73px">
  <div class="service-icon"><svg width="30" height="34" viewBox="0 0 30 34"><rect x="5" y="2" width="20" height="30" fill="#fff"/><g fill="#b5443d"><rect x="9" y="7" width="4" height="4"/><rect x="17" y="7" width="4" height="4"/><rect x="9" y="14" width="4" height="4"/><rect x="17" y="14" width="4" height="4"/><rect x="13" y="24" width="4" height="8"/></g></svg></div>
  <div class="service-name">Build and Renovate</div>
  <p class="service-text">Lorem ipsum dolor sit amet, consectetur adipising elit, sed do eiusmod tempor iunt ut labore et dolore magna</p>
</div>
<div class="service" style="left:341px">
  <div class="service-icon"><svg width="36" height="32" viewBox="0 0 36 32"><polygon points="18,2 2,16 7,16 7,30 15,30 15,21 21,21 21,30 29,30 29,16 34,16" fill="#fff"/></svg></div>
  <div class="service-name">New and Existing Homes</div>
  <p class="service-text">Lorem ipsum dolor sit amet, consectetur adipising elit, sed do eiusmod tempor iunt ut labore et dolore magna</p>
</div>
<div class="service" style="left:609px">
  <div class="service-icon"><svg width="36" height="34" viewBox="0 0 36 34"><circle cx="14" cy="20" r="9" fill="none" stroke="#fff" stroke-width="5" stroke-dasharray="4 3"/><circle cx="14" cy="20" r="3" fill="#fff"/><circle cx="27" cy="9" r="5" fill="none" stroke="#fff" stroke-width="3.5" stroke-dasharray="3 2"/></svg></div>
  <div class="service-name">Commercial Construction</div>
  <p class="service-text">Lorem ipsum dolor sit amet, consectetur adipising elit, sed do eiusmod tempor iunt ut labore et dolore magna</p>
</div>
<div class="service" style="left:877px">
  <div class="service-icon"><svg width="32" height="32" viewBox="0 0 32 32"><rect x="3" y="14" width="6" height="15" fill="none" stroke="#fff" stroke-width="2"/><path d="M11 15 L16 4 Q19 3 19 7 L18 12 L27 12 Q30 13 29 16 L26 27 Q25 29 22 29 L11 29 Z" fill="none" stroke="#fff" stroke-width="2" stroke-linejoin="round"/></svg></div>
  <div class="service-name">New Home &amp; Remodel</div>
  <p class="service-text">Lorem ipsum dolor sit amet, consectetur adipising elit, sed do eiusmod tempor iunt ut labore et dolore magna</p>
</div>

<section class="projects">
  <h2 class="section-title" style="top:50px">Recent <em>Projects</em></h2>
  <div class="project" style="left:89px"><div class="project-photo" role="img" aria-label="Kitchen with wooden cabinets and timber floor" style="background:linear-gradient(160deg,#8a5a3a,#c79a6a)"></div><div class="project-label">Neque porro quisquam<span class="project-go"></span></div></div>
  <div class="project" style="left:346px"><div class="project-photo" role="img" aria-label="Bright white bathroom with freestanding tub" style="background:linear-gradient(160deg,#dfe3e4,#b8bfc2)"></div><div class="project-label">Neque porro quisquam<span class="project-go"></span></div></div>
  <div class="project" style="left:605px"><div class="project-photo" role="img" aria-label="Modern kitchen with dark counters and pendant lights" style="background:linear-gradient(160deg,#6f6a66,#a8a29c)"></div><div class="project-label">Neque porro quisquam<span class="project-go"></span></div></div>
  <div class="project" style="left:864px"><div class="project-photo" role="img" aria-label="Living room with fireplace and built-in shelving" style="background:linear-gradient(160deg,#5a4538,#cbbfb0)"></div><div class="project-label">Neque porro quisquam<span class="project-go"></span></div></div>
  <svg class="abs" style="left:42px;top:230px" width="20" height="40" viewBox="0 0 20 40"><polyline points="16,2 4,20 16,38" fill="none" stroke="#aaa" stroke-width="1.5"/></svg>
  <svg class="abs" style="left:1138px;top:230px" width="20" height="40" viewBox="0 0 20 40"><polyline points="4,2 16,20 4,38" fill="none" stroke="#aaa" stroke-width="1.5"/></svg>
</section>

<section class="testimonial" role="img" aria-label="Red tinted city skyline backdrop">
  <svg class="abs" style="left:498px;top:80px" width="20" height="28" viewBox="0 0 20 28"><polyline points="15,3 5,14 15,25" fill="none" stroke="#fff" stroke-width="3"/></svg>
  <div class="avatar" role="img" aria-label="Portrait of a smiling client"></div>
  <svg class="abs" style="left:692px;top:80px" width="20" height="28" viewBox="0 0 20 28"><polyline points="5,3 15,14 5,25" fill="none" stroke="#fff" stroke-width="3"/></svg>
  <p class="quote">❝ Lorem Ipsum has been the industry's standard dummy text ever since the 1500s, when an unknown printer took a galley of type and scrambled it to make a type specimen book. It has survived not only five centuries, but also the leap into electronic typesetting, remaining essentially unchanged. It was popularised in the 1960s with the release of Letraset sheets containing Lorem Ipsum passages, and more recently with desktop publishing software ❞</p>
  <p class="quote-by">Neque porro quisquam est</p>
</section>

<h2 class="section-title" style="top:1904px">Latest <em>Blog</em></h2>

<article class="post" style="left:84px">
  <div class="post-photo" role="img" aria-label="Empty room with ladder and boxes" style="background:linear-gradient(180deg,#e8e8e6,#c7a57a)"><div class="post-date"><span class="day">02<small>JUN</small></span><span class="year">2016</span></div></div>
  <h3 class="post-title">Neque porro quisquam est qui dolorem</h3>
  <p class="post-text">Lorem Ipsum has been the industry's standard dummy text ever since the 1500s, when an unknown printer took a galley of type and scrambled it to make a type specimen book.</p>
  <p class="post-more">Read More »</p>
</article>
<article class="post" style="left:438px">
  <div class="post-photo" role="img" aria-label="Builder with tool belt holding a drill" style="background:linear-gradient(180deg,#d9c4a4,#c59a48)"><div class="post-date"><span class="day">02<small>JUN</small></span><span class="year">2016</span></div></div>
  <h3 class="post-title">Neque porro quisquam est qui dolorem</h3>
  <p class="post-text">Lorem Ipsum has been the industry's standard dummy text ever since the 1500s, when an unknown printer took a galley of type and scrambled it to make a type specimen book.</p>
  <p class="post-more">Read More »</p>
</article>
<article class="post" style="left:791px">
  <div class="post-photo" role="img" aria-label="Roofer working on a roof" style="background:linear-gradient(180deg,#b9bcbf,#5c5b5a)"><div class="post-date"><span class="day">02<small>JUN</small></span><span class="year">2016</span></div></div>
  <h3 class="post-title">Neque porro quisquam est qui dolorem</h3>
  <p class="post-text">Lorem Ipsum has been the industry's standard dummy text ever since the 1500s, when an unknown printer took a galley of type and scrambled it to make a type specimen book.</p>
  <p class="post-more">Read More »</p>
</article>

<footer class="site-footer">
  <div class="footer-col" style="left:89px">
    <h4>Links</h4>
    <ul class="footer-links"><li>Customer Support</li><li>Documentation</li><li>Resources</li><li>General FAQs</li><li>Shortcodes</li></ul>
  </div>
  <div class="footer-col" style="left:300px;width:232px">
    <h4>Renovate New</h4>
    <p class="footer-text">Lorem Ipsum has been the industry's standard dummy text ever since the 1500s, when an unknown printer took a galley of type and scrambled it to make a type specimen book. It has survived not only five centuries.</p>
  </div>
  <div class="footer-col" style="left:652px;width:200px">
    <h4>Get in Touch</h4>
    <p class="footer-text" style="text-align:left;line-height:20px">DEAN HARLOW MANAGER<br><br>Address : 1420 Harbour Street,<br>Sydney, NSW<br><br>Phone : 0400555019<br><br>Email :admin@marlowbuilding.example</p>
  </div>
  <div class="footer-col" style="left:907px;width:210px">
    <h4>Newsletter</h4>
    <p class="footer-text" style="text-align:left">Your about us information would fit here nicely</p>
    <div class="newsletter"><input type="text" placeholder="Email address"><button>Submit</button></div>
    <div class="social"><span></span><span></span><span></span></div>
  </div>
</footer>
<div class="footer-bottom">Copyright © 2016. All Rights Reserved</div>

</body>
</html>
```